Harvest Lantern Ministry Conference

I am in need of promotional graphics for our upcoming event. This event, titled "Harbor Crest Youth Conference", is a weekend event for teenagers 11-19 years old. They hear from religious speakers, listen to a band, and do other fun activities. Graphic design should be geared to young adults/older teens. Alcohol, drugs, smoking are not permitted. Open to any color combinations you think fit with your design.
Event Info:
November 1-3, 2024
Tellwood Exhibit Hall, Alder Springs, MN
Speakers: Marcus Linden (man in light blue shirt in attached photo), Tessa Vandermeer (woman in attached photo), Colin Hardy ( man in dark colored shirt in attached photo)
Worship: KW Collective
HarborCrestGather.com
#742GR
Our Organization Logo (attached): Lumenward
Once designed, I need the following graphics file sizes:
-11x17 Vertical Poster design: include all event info AND a "blank" space on the bottom or box for groups to add their own details/information. Also include the QRV logo and our organization logo Lumenward in some way.
-Make an additional copy of the 11x17 pdf with cut and bleed lines for printing, please.
-4x3 horizontal postcard: include all event info on 1 side including Lumenward logo and QRV; blank backside
-Main Graphic Slide: formatted to fit a widescreen 16x9 screen. Include event name, hashtag, QRV and Lumenward logo
-social media graphic(s) for event: can incorporate some or all of the event details. WILLING TO ADJUST BUDGET FOR SOCIAL MEDIA graphics.
-4.25in x 2.75in vertical badge: include event title on front with Lumenward logo
Target Market
ages 11-19
Target Market(s)
11-19 years old
Industry/Entity Type
Christian Youth Ministry

```html
<!DOCTYPE html>
<html lang="en">
<head>
<meta charset="utf-8">
<title>Harbor Crest Youth Conference</title>
<link href="https://fonts.googleapis.com/css2?family=Arimo:wght@400;700&family=Kaushan+Script&display=swap" rel="stylesheet">
<style>
  :root {
    --orange: #e5871f;
    --band-blue: #0295d5;
    --title-blue: #0a55b0;
    --navy: #163c78;
    --date-yellow: #ffbf00;
    --date-ring: #c9ecef;
    --date-blue: #1799d8;
    --frame-blue: #4a90e0;
    --note-fill: #c6e9f8;
    --note-line: #5ef02a;
    --ink: #111111;
    --white: #ffffff;
  }
  * { margin: 0; padding: 0; box-sizing: border-box; }
  html, body { width: 772px; height: 1200px; overflow: hidden; background: var(--orange); }
  .poster { position: relative; width: 772px; height: 1200px; background: var(--orange); font-family: "Arimo", Arial, sans-serif; overflow: hidden; }

  .hero { position: absolute; left: 0; top: 0; width: 772px; height: 429px;
    background:
      radial-gradient(ellipse at 30% 10%, #fff3a0 0%, rgba(255,214,70,0.7) 25%, rgba(0,0,0,0) 55%),
      radial-gradient(ellipse at 80% 40%, #ffc640 0%, rgba(0,0,0,0) 50%),
      linear-gradient(180deg, #f7a524 0%, #e67a12 55%, #5a2a10 85%, #2a1408 100%); }

  .event-title { position: absolute; left: 0; top: 22px; width: 772px; height: 240px; text-align: center; }
  .event-title .place { display: block; font-family: "Arimo", Arial, sans-serif; font-weight: 700; color: var(--title-blue);
    font-size: 98px; line-height: 76px; letter-spacing: -2px; }
  .event-title .kind { position: absolute; left: 168px; top: 150px; font-family: "Kaushan Script", cursive;
    color: var(--ink); font-size: 70px; line-height: 80px; transform: rotate(-9deg); transform-origin: left center; white-space: nowrap; }

  .info-band { position: absolute; left: 0; top: 429px; width: 772px; height: 172px; background: var(--band-blue); }
  .date-badge { position: absolute; left: 116px; top: 411px; width: 202px; height: 202px; border-radius: 50%;
    background: var(--date-yellow); border: 5px solid var(--date-ring); text-align: center; font-family: "Arimo", Arial, sans-serif; font-weight: 700; }
  .date-badge .days { display: block; color: var(--title-blue); font-size: 64px; line-height: 62px; margin-top: 24px; }
  .date-badge .month { display: block; color: var(--date-blue); font-size: 31px; line-height: 30px; letter-spacing: -1.5px; }
  .date-badge .year { display: block; color: var(--title-blue); font-size: 54px; line-height: 54px; letter-spacing: -1px; }
  .venue { position: absolute; left: 362px; top: 484px; color: var(--white);
    font-weight: 700; font-size: 26px; line-height: 35px; letter-spacing: -0.5px; }

  .speakers-heading { position: absolute; left: 0; top: 626px; width: 772px; text-align: center; color: var(--navy);
    font-weight: 700; font-size: 20px; letter-spacing: 19px; padding-left: 19px; }
  .speaker { position: absolute; top: 676px; width: 159px; }
  .speaker .portrait { width: 159px; height: 210px; border: 5px solid var(--frame-blue); }
  .speaker .name { position: absolute; top: 228px; left: -40px; width: 239px; text-align: center; color: var(--navy);
    font-weight: 700; font-size: 21px; white-space: nowrap; }
  .speaker-1 { left: 87px; } .speaker-2 { left: 309px; } .speaker-3 { left: 531px; }
  .speaker-1 .portrait { background: linear-gradient(160deg, #b9cde0 0%, #7fa6c8 45%, #5a7ea3 100%); }
  .speaker-2 .portrait { background: linear-gradient(170deg, #f2eee8 0%, #e4d6c4 50%, #f4f1ec 100%); }
  .speaker-3 .portrait { background: linear-gradient(170deg, #5a4a3a 0%, #3a3530 45%, #1c2130 100%); }

  .partners { position: absolute; left: 0; top: 960px; width: 772px; display: flex; justify-content: center; gap: 60px; align-items: center; }
  .partner-name { font-weight: 700; font-size: 34px; color: var(--navy); }

  .event-contact { position: absolute; left: 86px; top: 1074px; color: var(--navy); font-weight: 700; font-size: 21px; line-height: 28px; }
  .event-contact .mail-icon { display: inline-block; vertical-align: -1px; margin-right: 6px; }

  .group-note { position: absolute; left: 395px; top: 1067px; width: 299px; height: 97px; background: var(--note-fill);
    border: 2px solid var(--note-line); padding: 8px 12px; color: var(--navy); font-weight: 700; font-size: 19px; }
</style>
</head>
<body>
<main class="poster">
  <div class="hero" role="img" aria-label="Concert crowd with raised hands silhouetted against warm golden stage lights"></div>

  <h1 class="event-title">
    <span class="place">HARBOR<br>CREST</span>
    <span class="kind">Youth Conference</span>
  </h1>

  <section class="info-band"></section>
  <div class="date-badge">
    <span class="days">1-3</span>
    <span class="month">NOVEMBER</span>
    <span class="year">2024</span>
  </div>
  <p class="venue">TELLWOOD EXHIBIT HALL,<br>ALDER SPRINGS, MN</p>

  <h2 class="speakers-heading">SPEAKERS</h2>
  <figure class="speaker speaker-1">
    <div class="portrait" role="img" aria-label="Portrait of speaker Marcus Linden in a light blue shirt holding a microphone"></div>
    <figcaption class="name">Marcus Linden</figcaption>
  </figure>
  <figure class="speaker speaker-2">
    <div class="portrait" role="img" aria-label="Portrait of speaker Tessa Vandermeer in a white sweater"></div>
    <figcaption class="name">Tessa Vandermeer</figcaption>
  </figure>
  <figure class="speaker speaker-3">
    <div class="portrait" role="img" aria-label="Portrait of speaker Colin Hardy in a dark shirt"></div>
    <figcaption class="name">Colin Hardy</figcaption>
  </figure>

  <div class="partners">
    <span class="partner-name">Lumenward</span>
    <span class="partner-name">QRV</span>
  </div>

  <div class="event-contact">
    <p>Worship : KW Collective</p>
    <p><svg class="mail-icon" width="18" height="13" viewBox="0 0 18 13"><rect x="0.75" y="0.75" width="16.5" height="11.5" fill="none" stroke="currentColor" stroke-width="1.5"/><path d="M1 1 L9 7.5 L17 1" fill="none" stroke="currentColor" stroke-width="1.5"/></svg>harborcrestgather.com</p>
    <p>#742GR</p>
  </div>

  <div class="group-note">Group Info :</div>
</main>
</body>
</html>
```